Law Firm Website

Our client has never had a website, but their services are similar to: https://www.tallbrook-vance.com.

They are a personal injury attorney, husband, and wife team.

Coding

Coded - Design and coding required

Number of Pages Required

1 page

Font styles to use
Sans Serif

Colors
0054AA
0677BA
7BADD7
CADEEF
E8F1F8

```html
<!DOCTYPE html>
<html lang="en">
<head>
<meta charset="utf-8">
<title>Harborline Law — Personal Injury Attorneys</title>
<link rel="stylesheet" href="https://fonts.googleapis.com/css2?family=Ubuntu:wght@400;500&family=Lato:ital,wght@0,400;0,700;1,400&family=Roboto:ital,wght@0,300;0,400;1,300&display=swap">
<style>
:root{
  --navy:#0f1e38;
  --navy-deep:#050a3b;
  --ink:#0c1a33;
  --gold:#dba94b;
  --blue:#0677BA;
  --blue-dark:#0054AA;
  --blue-light:#7BADD7;
  --pale:#CADEEF;
  --paler:#E8F1F8;
  --grey:#5b5f66;
  --white:#ffffff;
}
*{margin:0;padding:0;box-sizing:border-box}
html,body{width:1200px;height:3203px;overflow:hidden;background:var(--white)}
body{position:relative;font-family:"Lato",sans-serif;color:var(--ink)}
.abs{position:absolute}
.heading{font-family:"Ubuntu",sans-serif;font-weight:500}

/* nav */
.site-nav{position:absolute;left:0;top:0;width:1200px;height:72px;background:var(--white)}
.brand{position:absolute;left:257px;top:26px;display:flex;align-items:center;gap:6px;font-family:"Lato",sans-serif;font-weight:700;font-size:14px;letter-spacing:2px;color:var(--blue-dark)}
.brand-dot{width:12px;height:12px;background:var(--blue-dark);border-radius:50%}
.nav-link{position:absolute;top:31px;font-size:12px;color:var(--ink);text-decoration:none}

/* hero */
.hero{position:absolute;left:0;top:72px;width:1200px;height:603px;background:radial-gradient(ellipse at 40% 30%,#4b5a72 0%,#2b3a54 35%,#15233e 75%,#0f1c35 100%)}
.hero-title{position:absolute;left:0;width:1200px;top:186px;text-align:center;color:var(--white);font-size:40px}
.hero-text{position:absolute;left:338px;width:524px;top:253px;text-align:center;color:var(--white);font-size:12.5px;line-height:15px}
.btn{position:absolute;background:var(--gold);color:var(--white);text-align:center;font-family:"Lato",sans-serif;text-transform:uppercase;border-radius:2px}
.hero-btn{left:543px;top:325px;width:112px;height:30px;line-height:30px;font-size:11px;font-weight:700}

/* about */
.about-photo{left:298px;top:721px;width:272px;height:210px;background:linear-gradient(90deg,#f3f4f6 0%,#e9eaec 40%,#2a2d33 60%,#1a1c21 100%)}
.about-title{left:618px;top:724px;font-size:20px;line-height:27px;color:var(--ink)}
.about-text{left:618px;top:805px;width:320px;font-size:11px;line-height:15px;color:var(--ink)}
.check-item{position:absolute;font-size:9px;font-style:italic;text-transform:uppercase;color:#444;display:flex;align-items:center;gap:6px}
.check-item svg{width:9px;height:9px}
.stat{position:absolute;width:200px;text-align:center}
.stat-num{color:var(--gold);font-size:19px;font-family:"Roboto",sans-serif;font-weight:300}
.stat-label{font-size:8.5px;font-style:italic;text-transform:uppercase;color:#444;margin-top:1px}
.stat-rule{position:absolute;top:965px;width:1px;height:62px;background:var(--pale)}

/* practice */
.practice{position:absolute;left:0;top:1089px;width:1200px;height:525px;background:linear-gradient(120deg,#2f3a4c 0%,#1a2a44 35%,#0f213f 65%,#0a1a36 100%)}
.practice-title{position:absolute;left:0;width:1200px;top:63px;text-align:center;color:var(--white);font-size:20px}
.gold-v{position:absolute;left:599px;top:145px;width:1.5px;height:318px;background:var(--gold)}
.gold-h{position:absolute;left:439px;top:304px;width:320px;height:1.5px;background:var(--gold)}
.area{position:absolute;width:260px;color:var(--white)}
.area h3{font-family:"Ubuntu",sans-serif;font-weight:500;font-size:20px;margin-bottom:9px}
.area p{font-family:"Roboto",sans-serif;font-size:9.5px;line-height:12px;width:238px}
.area.right-align{text-align:right}
.area.right-align p{margin-left:auto}
.area p.narrow{width:212px}

/* who */
.who-title{left:256px;width:334px;top:1678px;text-align:center;font-size:20px;color:var(--ink)}
.who-text{left:256px;top:1728px;width:320px;font-family:"Roboto",sans-serif;font-size:9.6px;line-height:15px;color:var(--grey)}
.who-photo{left:599px;top:1614px;width:601px;height:453px;background:linear-gradient(90deg,#c9d3dd 0%,#a9b7c6 45%,#2a4a86 75%,#d8dfe6 100%)}

/* cta */
.cta{position:absolute;left:0;top:2067px;width:1200px;height:156px;background:linear-gradient(90deg,#3a3e40 0%,#1d2b46 25%,#12244a 50%,#1d2b46 75%,#3a3e40 100%)}
.cta-title{position:absolute;left:0;width:1182px;top:24px;text-align:center;color:var(--white);font-size:20px}
.cta-sub{position:absolute;left:0;width:1188px;top:64px;text-align:center;color:var(--white);font-size:11px}
.cta-btn{left:551px;top:104px;width:86px;height:21px;line-height:21px;font-size:8.5px}

/* reviews */
.reviews-title{left:0;width:1200px;top:2288px;text-align:center;font-size:20px;color:var(--ink)}
.quote{left:310px;top:2385px;width:580px;text-align:center;font-family:"Roboto",sans-serif;font-weight:300;font-style:italic;font-size:20px;line-height:32.5px;color:#333}
.arrow{position:absolute;top:2538px;width:18px;height:30px}
.avatar{left:552px;top:2546px;width:94px;height:94px;border-radius:50%;background:radial-gradient(circle at 50% 40%,#6b5040 0%,#2c2a3a 60%,#e9ecf0 100%)}
.reviewer{left:0;width:1200px;top:2649px;text-align:center;font-family:"Roboto",sans-serif;font-style:italic;font-weight:300;font-size:20px;color:var(--blue)}
.dot{position:absolute;top:2706px;width:10px;height:10px;border-radius:50%;background:#d9d9d9}
.dot.active{background:var(--gold)}

/* footer */
.site-footer{position:absolute;left:0;top:2938px;width:1200px;height:265px;background:var(--navy-deep);color:var(--white)}
.footer-col{position:absolute;top:66px}
.footer-col h4{font-family:"Ubuntu",sans-serif;font-weight:400;font-size:20px;margin-bottom:8px}
.footer-col ul{list-style:none;padding-left:6px}
.footer-col li{font-family:"Roboto",sans-serif;font-size:14px;line-height:22.4px}
</style>
</head>
<body>

<header class="site-nav">
  <div class="brand"><span class="brand-dot"></span>HARBORLINE LAW</div>
  <a class="nav-link" style="left:571px" href="#">About</a>
  <a class="nav-link" style="left:671px" href="#">Services</a>
  <a class="nav-link" style="left:785px" href="#">Reviews</a>
  <a class="nav-link" style="left:898px" href="#">Contact</a>
</header>

<section class="hero" role="img" aria-label="Dark blue-toned photo of a Lady Justice statue holding scales">
  <h1 class="hero-title heading">Championing Your Rights Together</h1>
  <p class="hero-text">As a husband and wife team of experienced injury lawyers, we are dedicated to providing personalized and compassionate legal representation to help you get the justice and compensation you deserve.</p>
  <div class="btn hero-btn">Contact Us</div>
</section>

<section class="about">
  <div class="abs about-photo" role="img" aria-label="Two lawyers in dark suits standing with arms crossed"></div>
  <h2 class="abs about-title heading">We Are Professional Law Firm<br>Since 2015</h2>
  <p class="abs about-text">A lawyer is an expert who has the necessary qualifications to provide legal counsel and act on behalf of individuals and organizations in legal affairs.</p>
  <div class="check-item" style="left:618px;top:872px"><svg viewBox="0 0 10 10"><path d="M1 5l3 3 5-6" fill="none" stroke="#dba94b" stroke-width="1.3"/></svg>Excellence</div>
  <div class="check-item" style="left:618px;top:893px"><svg viewBox="0 0 10 10"><path d="M1 5l3 3 5-6" fill="none" stroke="#dba94b" stroke-width="1.3"/></svg>Integrity</div>
  <div class="check-item" style="left:618px;top:914px"><svg viewBox="0 0 10 10"><path d="M1 5l3 3 5-6" fill="none" stroke="#dba94b" stroke-width="1.3"/></svg>Accountability</div>
  <div class="check-item" style="left:791px;top:874px"><svg viewBox="0 0 10 10"><path d="M1 5l3 3 5-6" fill="none" stroke="#dba94b" stroke-width="1.3"/></svg>Trusted</div>
  <div class="check-item" style="left:791px;top:895px"><svg viewBox="0 0 10 10"><path d="M1 5l3 3 5-6" fill="none" stroke="#dba94b" stroke-width="1.3"/></svg>Certified</div>
  <div class="check-item" style="left:791px;top:916px"><svg viewBox="0 0 10 10"><path d="M1 5l3 3 5-6" fill="none" stroke="#dba94b" stroke-width="1.3"/></svg>Experienced</div>

  <div class="stat" style="left:269px;top:980px"><div class="stat-num">10+</div><div class="stat-label">Years of Experience</div></div>
  <div class="stat-rule" style="left:484px"></div>
  <div class="stat" style="left:500px;top:980px"><div class="stat-num">110</div><div class="stat-label">Trusted Clients</div></div>
  <div class="stat-rule" style="left:714px"></div>
  <div class="stat" style="left:733px;top:978px"><div class="stat-num">95%</div><div class="stat-label">Cases Won</div></div>
</section>

<section class="practice" role="img" aria-label="Dark blue photo of a hand resting on a law book">
  <h2 class="practice-title heading">Legal Practice Areas</h2>
  <div class="gold-v"></div>
  <div class="gold-h"></div>
  <div class="area right-align" style="left:303px;top:198px"><h3>Domestic Violence</h3><p class="narrow">Domestic battery, corporal injury to a spouse or cohabitant.</p></div>
  <div class="area" style="left:638px;top:198px"><h3>Personal Injury</h3><p>Law relating to physical or psychological injury due to the actions</p></div>
  <div class="area right-align" style="left:303px;top:337px"><h3>Theft</h3><p>Defenses for petty theft, grand theft, robbery, burglary, auto burglary, embezzlement.</p></div>
  <div class="area" style="left:638px;top:337px"><h3>Juvenile Crimes</h3><p class="narrow">Proceedings, wards of the court, sealing of juvenile records</p></div>
</section>

<section class="who">
  <h2 class="abs who-title heading">Who we are?</h2>
  <p class="abs who-text">A lawyer or attorney is a person who practices law, as an advocate, attorney, attorney at law, barrister, barrister-at-law, bar-at-law, civil law notary, counsel, counselor, counselor, counselor at law, solicitor, chartered legal executive, or public servant preparing, interpreting and applying law, but not as a paralegal or charter executive secretary. Working as a lawyer involves the practical application of abstract legal theories and knowledge to solve specific individualized problems, or to advance the interests of those who hire lawyers to perform legal services. A lawyer or attorney is a person who practices law, as an advocate, attorney, attorney at law, barrister, barrister-at-law, bar-at-law, civil law notary, counsel, counselor, counselor, counselor at law, solicitor, chartered legal executive, or public servant preparing, interpreting and applying law, but not as a paralegal or charter executive secretary.</p>
  <div class="abs who-photo" role="img" aria-label="Smiling lawyer in a blue suit with arms crossed in a bright office"></div>
</section>

<section class="cta" role="img" aria-label="Dark blue photo of brass scales of justice">
  <h2 class="cta-title heading">Contact us today to pursue the justice you deserve.</h2>
  <p class="cta-sub">And to empower yourself to attain equitable and impartial outcomes.</p>
  <div class="btn cta-btn">Contact Us</div>
</section>

<section class="reviews">
  <h2 class="abs reviews-title heading">What Client Say About Us</h2>
  <p class="abs quote">“During my recent legal matter, I appreciated the professionalism and expertise displayed by the individuals involved. They were readily available to address any concerns I had, which provided me with a sense of relief during a challenging period.”</p>
  <svg class="arrow" style="left:240px" viewBox="0 0 18 30"><path d="M16 2L3 15l13 13" fill="none" stroke="#dba94b" stroke-width="2"/></svg>
  <svg class="arrow" style="left:942px" viewBox="0 0 18 30"><path d="M2 2l13 13L2 28" fill="none" stroke="#dba94b" stroke-width="2"/></svg>
  <div class="abs avatar" role="img" aria-label="Portrait of the reviewing client"></div>
  <div class="abs reviewer">Mara Ellison</div>
  <span class="dot active" style="left:566px"></span>
  <span class="dot" style="left:594px"></span>
  <span class="dot" style="left:623px"></span>
</section>

<footer class="site-footer">
  <div class="footer-col" style="left:256px"><h4>Menu</h4><ul><li>Link 1</li><li>Link 2</li><li>Link 3</li><li>Link 4</li><li>Link 5</li></ul></div>
  <div class="footer-col" style="left:397px"><h4>Useful Links</h4><ul><li>Terms &amp; Conditions</li><li>Privacy Policy</li><li>Disclaimer</li><li>FAQ</li></ul></div>
  <div class="footer-col" style="left:623px"><h4>Follow Us</h4><ul><li>Friendnet</li><li>Chirper</li><li>Snapgram</li><li>Workline</li></ul></div>
  <div class="footer-col" style="left:805px"><h4>Contact Us</h4><ul><li>email:</li><li>hello@harborline-law.com</li><li>&nbsp;</li><li>phone:</li><li>+1 555-014-8722</li></ul></div>
</footer>

</body>
</html>
```